Navigate the Underground Car Park to 7K3R Vet Clinic

Eye-catching signage for Underground Carpark.
We want to help new Clients, or those with bad senses of direction, to the correct Lift Lobby.
We want to be able to say 'Just follow the signs'.

It can be confusing and many other business have utilised some of the pillars in the carpark to guide their customers to the right place.

People don't want to walk far with sick animals so it is important they get to the right Lift Lobby.
Updates

We are thinking instead of 'Just Follow the Signs,We would like to try:'Looking for us?' (Large Text)'Follow the Signs (much smaller Text)Also, it is very useful to see the proposed sign dropped on to the photo of the car park pillars I included.Many thanks Added Friday, June 16, 2017

Target Market(s)

Customers, coming for the 1st time, trying to navigate the Underground CarPark towards the appropriate Lift lobby

Industry/Entity Type

Veterinary

Font styles to use
Serif

Colors
f78f20
00a990
0455a3

Requirements
Must have
• Logo.
• Bright. Clear. Not too cluttered.
• Warmth. Humour. Approachable.
• Please include: Building 4, Mezzanine Level
Nice to have
• Please look at our FB pages and Instagram page @7k3rvetclinic for a good feel of who we are.
• Some level of style or image continuity with the Pet Tips Poster (see attached file)
Should not have
• Not have a medical feel

```html
<!DOCTYPE html>
<html lang="en">
<head>
<meta charset="utf-8">
<title>7K3R Vet Clinic – Parking Wayfinding Sign</title>
<link rel="stylesheet" href="https://fonts.googleapis.com/css2?family=Montserrat:wght@600;800&family=Quicksand:wght@600;700&display=swap">
<style>
  :root {
    --orange: #f78f20;
    --teal: #00a990;
    --blue: #0455a3;
    --ink: #2f2a4a;
    --paper: #ffffff;
    --backdrop: #c3cad6;
    --fur-light: #e8cfa4;
    --fur-dark: #c98a4b;
    --ring-teal: #6fa7a0;
  }
  * { box-sizing: border-box; margin: 0; padding: 0; }
  html, body { width: 1200px; height: 1200px; overflow: hidden; }
  body { background: var(--backdrop); position: relative; font-family: "Montserrat", sans-serif; }

  .sign {
    position: absolute; left: 180px; top: 30px;
    width: 840px; height: 1140px;
    background: var(--paper);
    box-shadow: 0 10px 30px rgba(40, 50, 70, .25);
    overflow: hidden;
  }

  .brand {
    position: absolute; left: 120px; top: 120px;
    display: flex; align-items: center; gap: 14px;
    font-family: "Quicksand", sans-serif; font-weight: 700;
    font-size: 46px; color: var(--teal);
  }
  .brand__dot { width: 30px; height: 30px; border-radius: 50%; background: var(--teal); }

  .photo { position: absolute; }
  .photo--puppy {
    right: 70px; top: 100px; width: 180px; height: 190px;
    background: radial-gradient(circle at 50% 40%, #f3e2c4, var(--fur-light) 60%, #fff 100%);
    border-radius: 40% 40% 8px 8px;
  }
  .photo--dog {
    left: 100px; top: 520px; width: 280px; height: 290px;
    background: radial-gradient(circle at 50% 40%, #dea469, var(--fur-dark) 65%, #b37238 100%);
    border-radius: 45% 45% 10px 10px;
  }

  .headline-box {
    position: absolute; left: 40px; top: 280px; width: 760px; height: 200px;
    border: 5px solid var(--orange); border-radius: 22px;
    background: var(--paper);
    text-align: center; padding-top: 34px;
  }
  .headline-box__title {
    font-weight: 800; font-size: 66px; letter-spacing: 2px;
    color: var(--orange); line-height: 1;
  }
  .headline-box__sub {
    margin-top: 18px;
    font-weight: 600; font-size: 38px; letter-spacing: 9px;
    color: var(--teal);
  }

  .location-badge { position: absolute; left: 470px; top: 500px; width: 310px; height: 310px; }
  .location-badge text { font-family: "Montserrat", sans-serif; }

  .parking-arrow { position: absolute; left: 20px; top: 790px; width: 800px; height: 330px; }
  .parking-arrow text { font-family: "Montserrat", sans-serif; font-weight: 800; }
</style>
</head>
<body>
  <main class="sign">
    <div class="brand"><span class="brand__dot"></span>7K3R Vet Clinic</div>

    <div class="photo photo--puppy" role="img" aria-label="Photo of a smiling golden retriever puppy"></div>

    <section class="headline-box">
      <h1 class="headline-box__title">LOOKING FOR US?</h1>
      <p class="headline-box__sub">Follow the Signs</p>
    </section>

    <div class="photo photo--dog" role="img" aria-label="Photo of a friendly ginger dog with paws resting on the parking sign"></div>

    <svg class="location-badge" viewBox="0 0 310 310" aria-label="Situated in Silver Bay Arcade, Building 4, Mezzanine level, above Cafe Lumen">
      <defs>
        <path id="badge-top" d="M40,155 A115,115 0 0 1 270,155"/>
        <path id="badge-bottom" d="M28,155 A127,127 0 0 0 282,155"/>
      </defs>
      <circle cx="155" cy="155" r="150" fill="#fff" stroke="var(--ring-teal)" stroke-width="3"/>
      <circle cx="155" cy="155" r="146" fill="none" stroke="var(--ring-teal)" stroke-width="1.5" stroke-dasharray="3 5"/>
      <text font-size="30" font-weight="800" fill="var(--ink)" letter-spacing="3">
        <textPath href="#badge-top" startOffset="50%" text-anchor="middle">SITUATED IN</textPath>
      </text>
      <text font-size="28" font-weight="800" fill="var(--ring-teal)" letter-spacing="2">
        <textPath href="#badge-bottom" startOffset="50%" text-anchor="middle">SILVER BAY ARCADE</textPath>
      </text>
      <circle cx="155" cy="155" r="88" fill="var(--orange)"/>
      <text x="155" y="130" text-anchor="middle" font-size="16" font-weight="800" fill="#fff">Silver Bay Arcade</text>
      <text x="155" y="156" text-anchor="middle" font-size="16" font-weight="800" fill="#fff">Building 4</text>
      <text x="155" y="182" text-anchor="middle" font-size="16" font-weight="800" fill="#fff">Mezzanine level</text>
      <text x="155" y="202" text-anchor="middle" font-size="11" font-weight="600" fill="#fff">(Above Cafe Lumen)</text>
    </svg>

    <svg class="parking-arrow" viewBox="0 0 800 330" aria-label="Parking this way">
      <polygon class="parking-arrow__panel" points="0,0 680,0 800,165 680,330 0,330" fill="var(--blue)"/>
      <g class="car-icon" fill="#fff">
        <rect x="40" y="110" width="190" height="110" rx="28"/>
        <path d="M68,115 L90,60 Q95,50 108,50 L162,50 Q175,50 180,60 L202,115 Z"/>
        <rect x="50" y="215" width="34" height="34" rx="6"/>
        <rect x="186" y="215" width="34" height="34" rx="6"/>
      </g>
      <g fill="var(--blue)">
        <path d="M86,108 L102,66 L168,66 L184,108 Z"/>
        <rect x="90" y="160" width="90" height="26" rx="4"/>
        <ellipse cx="68" cy="150" rx="16" ry="10"/>
        <ellipse cx="202" cy="150" rx="16" ry="10"/>
      </g>
      <text x="250" y="262" font-size="240" fill="#fff">P</text>
      <text x="380" y="300" font-size="58" fill="#fff">arking</text>
      <polygon class="parking-arrow__chevron" points="610,40 652,40 742,165 652,290 610,290 700,165" fill="#fff"/>
    </svg>
  </main>
</body>
</html>
```